Web Design Project

Psychotherapy and Counselling Practice needs a landing page web design.

My business "Larkspur Advisory" specialises in the treatment of Anxiety and Depression with a holistic approach, endeavouring to unlock the key that holds us to ransom in a life that is imbalanced, frustrating, and ultimately of our own making due to our own perceptions and behaviours.

There is much that impacts us which we cannot change, but we are always in control of how we think, and how we frame our experiences.....learning to challenge those thoughts and behaviours that are destructive and disempowering opens up a world of joyful possibility. Life is about making choices, learn to make wiser and healthier choices.......

Larkspur Advisory has a client base of individual clients but will seek to expand to offer services to the Corporate world by offering an adjunct to employers for established "Wellness Programs".

Larkspur Advisory is a highly professional, ethically bound business, with the needs of the client at the forefront of all we do.

Larkspur Advisory wishes to avoid the usual "jargon driven" psychobabble offered on many counselling web pages. It aims to be stylishly presented, clean in look and with as few "words" as possible and a largely white background (faster loading and more powerful impact of what is stated), those words contained in the webpage should be meaningful, persuasive and have an impact simply at glance. Larkspur does not want , or expect, those prospective clients in need of support , to be reading through volumes of industry driven cliches.

At this point Larkspur is just looking for a high quality landing page. However in time this will likely expand to include other sections such as case studies, video content etc.

Target Market(s)

Those in need of emotional support, suffering mental health issues, and those simply wanting to become self aware supported by a mindful therapist.

Industry/Entity Type

Industry

Requirements
Must have
• The design must incorporate the Larkspur logo and colour schemes found on the attached files.

```html
<!DOCTYPE html>
<html lang="en">
<head>
<meta charset="utf-8">
<title>Larkspur Advisory</title>
<link href="https://fonts.googleapis.com/css2?family=Heebo:wght@300;400;500&display=swap" rel="stylesheet">
<style>
  :root {
    --header-grey: #6c6c6c;
    --leaf: #a5b842;
    --leaf-light: #b7c955;
    --leaf-dark: #8ea534;
    --paper: #ffffff;
    --footer-stone: #e8e7e1;
    --body-text: #7b7b7b;
    --heading-text: #3c3c3c;
    --client-grey: #767676;
  }
  * { margin: 0; padding: 0; box-sizing: border-box; }
  html, body { width: 1200px; height: 1000px; overflow: hidden; }
  body {
    position: relative;
    background: var(--paper);
    font-family: "Heebo", Arial, sans-serif;
    color: var(--body-text);
  }
  .site-header {
    position: absolute; left: 0; top: 0; width: 1200px; height: 106px;
    background: var(--header-grey);
  }
  .brand-name {
    position: absolute; left: 125px; top: 30px;
    font-size: 38px; font-weight: 300; color: #fff; letter-spacing: -1px;
  }
  .brand-mark {
    position: absolute; left: 500px; top: 48px;
    font-size: 16px; font-weight: 300; color: #fff; letter-spacing: 0.5px;
    text-transform: uppercase;
  }
  .main-nav { position: absolute; top: 50px; left: 0; }
  .main-nav a {
    position: absolute; color: #fff; text-decoration: none;
    font-size: 14px; font-weight: 400; white-space: nowrap;
  }
  .hero-band {
    position: absolute; left: 0; top: 113px; width: 1200px; height: 181px;
    background: var(--leaf);
  }
  .service {
    position: absolute; top: 189px; width: 220px; height: 396px;
  }
  .service::after {
    content: ""; position: absolute; right: 0; top: 110px; width: 14px; height: 286px;
    background: linear-gradient(to right, rgba(0,0,0,0.08), rgba(0,0,0,0));
    transform: translateX(14px);
  }
  .service-badge {
    position: absolute; left: 0; top: 0; width: 206px; height: 206px;
    border-radius: 50%; background: var(--paper);
  }
  .service-badge-inner {
    position: absolute; left: 6px; top: 6px; width: 194px; height: 194px; border-radius: 50%;
    background: linear-gradient(to bottom, var(--leaf-light), var(--leaf-dark));
    display: flex; align-items: center; justify-content: center; text-align: center;
    color: #fff; font-size: 30px; font-weight: 300; line-height: 37px; letter-spacing: -0.5px;
  }
  .service-text {
    position: absolute; left: 0; top: 228px; width: 204px;
    font-size: 12px; line-height: 18px; text-align: justify; font-weight: 300;
  }
  .site-footer {
    position: absolute; left: 0; top: 640px; width: 1200px; height: 360px;
    background: var(--footer-stone);
  }
  .about-title {
    position: absolute; left: 129px; top: 663px; font-size: 14px; font-weight: 300; color: #777;
  }
  .about-text {
    position: absolute; left: 129px; top: 691px; width: 440px;
    font-size: 12px; line-height: 18px; text-align: justify; font-weight: 300;
  }
  .newsletter {
    position: absolute; left: 621px; top: 695px; width: 447px; height: 52px;
    background: #fff; border-radius: 3px; box-shadow: 0 2px 3px rgba(0,0,0,0.15);
  }
  .newsletter-icon { position: absolute; left: 20px; top: 20px; }
  .newsletter-label {
    position: absolute; left: 48px; top: 18px; font-size: 12px; color: #888; font-weight: 300;
  }
  .newsletter-join {
    position: absolute; right: 7px; top: 8px; width: 58px; height: 38px; border-radius: 3px;
    background: linear-gradient(to bottom, var(--leaf-light), var(--leaf-dark));
    border: 1px solid #7f9530;
    font-size: 14px; font-weight: 500; color: #46531a;
    display: flex; align-items: center; justify-content: center;
  }
  .clients-title {
    position: absolute; left: 620px; top: 810px; font-size: 14px; color: var(--heading-text); font-weight: 300;
  }
  .client-list { position: absolute; left: 620px; top: 848px; width: 449px; display: flex; justify-content: space-between; }
  .client-name { font-size: 22px; font-weight: 500; color: var(--client-grey); }
  .social { position: absolute; top: 941px; left: 482px; display: flex; gap: 11px; }
  .social a {
    width: 38px; height: 38px; border-radius: 50%; background: var(--leaf-dark);
    box-shadow: 3px 3px 0 rgba(0,0,0,0.15);
    display: flex; align-items: center; justify-content: center;
    color: #fff; font-size: 10px; font-weight: 400; text-decoration: none;
  }
</style>
</head>
<body>
  <header class="site-header">
    <div class="brand-name">Larkspur Advisory</div>
    <div class="brand-mark">Larkspur</div>
    <nav class="main-nav">
      <a style="left:738px">HOME</a>
      <a style="left:817px">ABOUT</a>
      <a style="left:902px">CONTACT</a>
      <a style="left:1004px">SERVICES</a>
    </nav>
  </header>

  <div class="hero-band"></div>

  <section class="service" style="left:128px">
    <div class="service-badge"><div class="service-badge-inner">Anxiety</div></div>
    <p class="service-text">Lorem ipsum dolor sit amet, consectetur adipiscing elit. Mauris interdum velit vitae nulla molestie eu commodo nulla dapibus. Donec id sollicitudin urna. Integer at dui ac leo fermentum varius eleifend ut libero. Mauris interdum velit vitae nulla molestie eu commodo nulla dapibus.</p>
  </section>
  <section class="service" style="left:496px">
    <div class="service-badge"><div class="service-badge-inner">Depression</div></div>
    <p class="service-text">Lorem ipsum dolor sit amet, consectetur adipiscing elit. Mauris interdum velit vitae nulla molestie eu commodo nulla dapibus. Donec id sollicitudin urna. Integer at dui ac leo fermentum varius eleifend ut libero. Mauris interdum velit vitae nulla molestie eu commodo nulla dapibus.</p>
  </section>
  <section class="service" style="left:864px">
    <div class="service-badge"><div class="service-badge-inner">Wellness<br>program</div></div>
    <p class="service-text">Lorem ipsum dolor sit amet, consectetur adipiscing elit. Mauris interdum velit vitae nulla molestie eu commodo nulla dapibus. Donec id sollicitudin urna. Integer at dui ac leo fermentum varius eleifend ut libero. Mauris interdum velit vitae nulla molestie eu commodo nulla dapibus.</p>
  </section>

  <footer class="site-footer"></footer>
  <h2 class="about-title">Lorem</h2>
  <p class="about-text">Lorem ipsum dolor sit amet, consectetur adipiscing elit. Mauris interdum velit vitae nulla molestie eu commodo nulla dapibus. Donec id sollicitudin urna. Integer at dui ac leo fermentum varius eleifend ut libero. Mauris interdum velit vitae nulla molestie eu commodo nulla dapibus.<br>Lorem ipsum dolor sit amet, consectetur adipiscing elit. Mauris interdum velit vitae nulla molestie eu commodo nulla dapibus. Donec id sollicitudin urna. Integer at dui ac leo fermentum varius eleifend ut libero. Mauris interdum velit vitae nulla molestie eu commodo nulla dapibus. Lorem ipsum dolor sit amet, consectetur adipiscing elit. Mauris interdum velit vitae nulla molestie eu commodo nulla dapibus. Donec id sollicitudin urna. Integer at dui ac leo fermentum varius eleifend ut libero. Mauris interdum velit vitae nulla molestie eu commodo nulla dapibus.</p>

  <div class="newsletter">
    <svg class="newsletter-icon" width="14" height="11" viewBox="0 0 14 11" aria-hidden="true">
      <rect x="0" y="0" width="14" height="11" rx="1" fill="#cfcfcf"/>
      <path d="M0.5 1 L7 6 L13.5 1" stroke="#fff" stroke-width="1.2" fill="none"/>
    </svg>
    <span class="newsletter-label">Join Our Newsletter Here</span>
    <span class="newsletter-join">Join</span>
  </div>

  <h3 class="clients-title">Our corporate clients</h3>
  <div class="client-list">
    <span class="client-name">Norvale</span>
    <span class="client-name">Halden</span>
    <span class="client-name">Quorra</span>
    <span class="client-name">Tessit</span>
  </div>

  <nav class="social">
    <a>Kite</a><a>Feed</a><a>Pals</a><a>Tack</a><a>Orbit</a>
  </nav>
</body>
</html>
```